Plakat-Design 24h Betreuung
Zielgruppe
Wir vermitteln 24h Pflege- und Betreuungskräfte für alte und hilfbedürftige Menschen!
Zielgruppe: deren Angehörige (zwischen 50-70 Jahre alt)
Aufgabenstellung
Klare Ansage - nicht zu verspielt - geradlinig
Maße Plakat: 504 cm breit x 238 cm hoch
Das PLAKAT ist ca 10 m von der Straße entfernet und ist für Autofahrer gedacht - somit muss man alles gut lesen können und groß geschrieben sein !!!!
Folgender Text und Bilder sollte das Plakat beinhalten:
24h - Betreuung (groß links oben platziert)
Logo: SorgeHafen.at
Foto mit 10 Personen
Erfahrung seit 2010
www.sorgehafen.at

```html
<!DOCTYPE html>
<html lang="de">
<head>
<meta charset="utf-8">
<title>24h - Betreuung – SorgeHafen.at</title>
<link rel="stylesheet" href="https://fonts.googleapis.com/css2?family=Montserrat:wght@600;700;800&display=swap">
<style>
  :root {
    --frame: #23262f;
    --paper: #ffffff;
    --navy: #2b4180;
    --orange: #d4671e;
    --photo-light: #eef0f5;
    --photo-mid: #c9d0df;
  }
  html, body {
    margin: 0;
    padding: 0;
    width: 1200px;
    height: 704px;
    overflow: hidden;
    background: var(--frame);
    font-family: "Montserrat", Arial, sans-serif;
  }
  .poster {
    position: absolute;
    left: 71px;
    top: 71px;
    width: 1058px;
    height: 561px;
    background: var(--paper);
    overflow: hidden;
  }
  .headline {
    position: absolute;
    left: 48px;
    top: 24px;
    margin: 0;
    font-weight: 800;
    font-size: 84px;
    line-height: 1;
    letter-spacing: 1px;
    color: var(--navy);
    white-space: nowrap;
  }
  .brand {
    position: absolute;
    left: 742px;
    top: 112px;
    font-weight: 700;
    font-size: 29px;
    letter-spacing: 0.5px;
    color: var(--navy);
  }
  .team-photo {
    position: absolute;
    left: 308px;
    top: 157px;
    width: 476px;
    height: 350px;
    border-radius: 40px 40px 20px 20px;
    background: radial-gradient(ellipse at 50% 45%, var(--photo-mid) 0%, var(--photo-light) 70%, var(--paper) 100%);
  }
  .shapes {
    position: absolute;
    left: 0;
    top: 0;
  }
  .experience {
    position: absolute;
    left: 26px;
    top: 394px;
    width: 200px;
    text-align: center;
    color: var(--paper);
  }
  .experience .label {
    font-weight: 600;
    font-size: 34px;
    line-height: 34px;
  }
  .experience .year {
    font-weight: 800;
    font-size: 60px;
    line-height: 64px;
    margin-top: 2px;
  }
  .web {
    position: absolute;
    left: 660px;
    top: 509px;
    font-weight: 800;
    font-size: 31px;
    color: var(--paper);
    letter-spacing: 0.3px;
  }
</style>
</head>
<body>
  <main class="poster">
    <h1 class="headline">24h - Betreuung</h1>
    <div class="brand">SorgeHafen.at</div>

    <div class="team-photo" role="img" aria-label="Gruppenfoto des Teams: zehn Personen in weißen Blusen und Jeans, vorne eine Dame im blauen Kostüm"></div>

    <svg class="shapes" width="1058" height="561" viewBox="0 0 1058 561" aria-hidden="true">
      <rect x="250" y="547" width="450" height="14" fill="var(--navy)"/>
      <circle cx="113" cy="488" r="158" fill="var(--orange)"/>
      <circle cx="113" cy="488" r="144" fill="var(--navy)"/>
      <path d="M 606 561 L 606 541 Q 606 501 646 501 L 1058 501 L 1058 561 Z" fill="var(--orange)"/>
    </svg>

    <div class="experience">
      <div class="label">Erfahrung<br>seit</div>
      <div class="year">2010</div>
    </div>

    <div class="web">www.sorgehafen.at</div>
  </main>
</body>
</html>
```